Design a Business Card

I would like a busniess card design for my new logo. Should be a stylish business card for a realestate investment company.
No specific colors.
Attached please find the logo.
Information that should be added:
Delira Vosloo
Tel: +27 82 514 6093
Email: [login to view URL]@[login to view URL]

```html
<!DOCTYPE html>
<html lang="en">
<head>
<meta charset="utf-8">
<title>Kestrella Business Card</title>
<link rel="stylesheet" href="https://fonts.googleapis.com/css2?family=Open+Sans:wght@300;400&display=swap">
<style>
  :root {
    --canvas-bg: #2b2d31;
    --card-bg: #0a0a0a;
    --ink: #f2f2f2;
    --ink-muted: #bdbdbd;
    --rule: #8a8a8a;
  }
  * { margin: 0; padding: 0; box-sizing: border-box; }
  html, body {
    width: 1200px; height: 900px; overflow: hidden;
    background: var(--canvas-bg);
    font-family: "Open Sans", sans-serif;
    color: var(--ink);
  }
  .canvas {
    width: 1200px; height: 900px;
    display: flex; align-items: center; justify-content: center; gap: 60px;
  }
  .card {
    width: 510px; height: 300px;
    background: var(--card-bg);
    border-radius: 22px;
    position: relative;
    box-shadow: 0 14px 30px rgba(0,0,0,0.45);
  }
  .brand {
    display: flex; align-items: center; justify-content: center; gap: 12px;
  }
  .brand-square {
    width: 16px; height: 16px; background: var(--ink);
  }
  .brand-name {
    font-weight: 300; letter-spacing: 4px; color: var(--ink);
  }
  .card-back .brand {
    position: absolute; inset: 0;
  }
  .card-back .brand-name { font-size: 38px; }
  .card-front .brand {
    position: absolute; top: 62px; left: 0; right: 0;
  }
  .card-front .brand-name { font-size: 30px; }
  .contact-block {
    position: absolute; left: 0; right: 0; top: 170px;
    display: flex; justify-content: center; align-items: center;
  }
  .person {
    text-align: right; padding-right: 22px;
  }
  .person-name { font-size: 17px; font-weight: 400; }
  .person-role { font-size: 13px; font-weight: 300; color: var(--ink-muted); margin-top: 2px; }
  .divider { width: 1px; height: 62px; background: var(--rule); }
  .details { padding-left: 22px; display: flex; flex-direction: column; gap: 10px; }
  .detail { display: flex; align-items: center; gap: 10px; font-size: 12.5px; font-weight: 300; }
  .detail-icon { width: 20px; height: 20px; flex: none; }
</style>
</head>
<body>
  <main class="canvas">
    <section class="card card-front">
      <div class="brand">
        <span class="brand-square"></span>
        <span class="brand-name">KESTRELLA</span>
      </div>
      <div class="contact-block">
        <div class="person">
          <p class="person-name">Delira Vosloo</p>
          <p class="person-role">CEO</p>
        </div>
        <div class="divider"></div>
        <div class="details">
          <p class="detail">
            <svg class="detail-icon" viewBox="0 0 20 20" aria-hidden="true">
              <circle cx="10" cy="10" r="10" fill="#f2f2f2"/>
              <path d="M7 5.5 L8.6 5.3 L9.4 7.6 L8.4 8.5 Q9.3 10.6 11.5 11.6 L12.4 10.6 L14.7 11.4 L14.5 13 Q13.5 14.5 11.5 14 Q6.5 12.4 5.9 7.6 Q5.8 6.2 7 5.5 Z" fill="#0a0a0a"/>
            </svg>
            <span>+27 82 514 6093</span>
          </p>
          <p class="detail">
            <svg class="detail-icon" viewBox="0 0 20 20" aria-hidden="true">
              <circle cx="10" cy="10" r="10" fill="#f2f2f2"/>
              <rect x="5" y="6.5" width="10" height="7" rx="1" fill="#0a0a0a"/>
              <path d="M5.3 7 L10 10.6 L14.7 7" stroke="#f2f2f2" stroke-width="1" fill="none"/>
            </svg>
            <span>office.kestrella@mailhub.com</span>
          </p>
        </div>
      </div>
    </section>
    <section class="card card-back">
      <div class="brand">
        <span class="brand-square"></span>
        <span class="brand-name">KESTRELLA</span>
      </div>
    </section>
  </main>
</body>
</html>
```